Data Center Operator to enter Indian Market needs a Client Sales Pitch Power Point Presentation

We need a Sales Client Pitch Powerpoint Corporate Presentation for a Data Center Operator to enter Indian Market, called Velorin Data Centers, in order to attract Potential Clients such who are Large Multinational IT Corporations (i.e. Streamvix, Quarnisoft, Dealwright, Pomelo, Zindex, KTR, Orinoco, Friendwall, CareerKnot, etc.). We have created a Base Presentation which includes all the text needed for our Sales Client Pitch.
We expect designers to provide us with a Finished Version of the Sale Client Pitch Presentation which includes our Text (which will include but not limited to: uniform of text, same font throughout, re-design of entire deck and slides, re-positioning of texts, adding symbols/images to certain bullet points to make the slide stand out more, making the presentation in line with our corporate colours (attached colour scheme)- Wine Burgundy and Grey, create fluidity between the slides, Re-design of Graphs to reflect new uniform of presentation, etc.)

Target Market(s)

Large IT Multinational Companies (i.e. Streamvix, Quarnisoft, Dealwright, Pomelo, Zindex, KTR, Orinoco, Friendwall, CareerKnot, etc.) who wish to enter the Indian Market and/or expand their presence in such Market.

Industry/Entity Type

It Company

Font styles to use
Sans Serif

Colors

Designer to choose colors to be used in the design.

Requirements
Must have
• - We would like for the Presentation to reflect us as the following: Dynamic, IT Company, High Technology, Professionalism, International Standard, Avant Garde Design, Modern Approach to evolving Market, Messages to be Loud and Clear to the Client.
• - Uniform of Text
• - Same font throughout
• - Re-design of entire deck and slides
• - Re-positioning of texts
• - Adding symbols/images to certain bullet points to make the slide stand out more
• - Making the presentation in line with our corporate colours (attached colour scheme) - Wine Burgundy and Grey
• - Create fluidity between the slides
• - Re-design of Graphs to reflect new uniform of presentation
Nice to have
• - A small text box which includes the source of information when referencing a statistic
Should not have
• - We do not want a Powerpoint Template, we require to view the finished version of the presentation which includes our text so we can present it to the Client.

```html
<!DOCTYPE html>
<html lang="en">
<head>
<meta charset="utf-8">
<title>Velorin Data Centers – Introduction</title>
<link rel="stylesheet" href="https://fonts.googleapis.com/css2?family=Exo+2:wght@600;700;800&family=Open+Sans:wght@400;700&display=swap">
<style>
  :root {
    --wine: #5c1520;
    --wine-bright: #8a1430;
    --grey-text: #6b6b6b;
    --ink: #1f1f1f;
    --map-grey: #e6e6e6;
    --dot-grey: #d4d4d4;
    --paper: #ffffff;
  }
  * { box-sizing: border-box; margin: 0; padding: 0; }
  html, body { width: 1200px; height: 720px; overflow: hidden; background: var(--paper); }
  .slide {
    position: relative; width: 1200px; height: 720px; overflow: hidden;
    background: radial-gradient(ellipse at 92% 18%, #ececec 0%, #ffffff 45%);
    font-family: "Open Sans", Arial, sans-serif;
  }
  .pin-badge {
    position: absolute; left: 44px; top: 32px; width: 58px; height: 68px;
    border-radius: 50% 50% 40% 40%;
    background: radial-gradient(circle at 40% 35%, #fafafa, #bdbdbd 75%);
  }
  .brand {
    position: absolute; left: 1000px; top: 40px; display: flex; align-items: center; gap: 8px;
    font-family: "Exo 2", sans-serif; font-weight: 700; font-size: 15px; line-height: 1.05;
    color: var(--wine); letter-spacing: 0.04em; text-transform: uppercase;
  }
  .brand-mark { width: 12px; height: 12px; background: var(--wine); }
  .title {
    position: absolute; left: 0; right: 0; top: 58px; text-align: center;
    font-family: "Exo 2", sans-serif; font-weight: 800; font-size: 60px; color: var(--wine);
    letter-spacing: -0.01em;
  }
  .subtitle {
    position: absolute; left: 0; right: 0; top: 128px; text-align: center;
    font-family: "Exo 2", sans-serif; font-weight: 700; font-size: 18px; color: var(--grey-text);
  }
  .slide-dots { position: absolute; left: 36px; top: 312px; width: 16px; }
  .slide-dots span { display: block; margin: 0 auto; border-radius: 50%; background: var(--dot-grey); }
  .slide-dots .d1 { width: 5px; height: 5px; margin-bottom: 14px; }
  .slide-dots .d2 { width: 8px; height: 8px; margin-bottom: 14px; }
  .slide-dots .active { width: 15px; height: 15px; background: var(--wine); margin-bottom: 12px; }
  .slide-dots .d4 { width: 9px; height: 9px; margin-bottom: 14px; }
  .slide-dots .d5 { width: 5px; height: 5px; }
  .india-map {
    position: absolute; left: 218px; top: 200px; width: 396px; height: 488px;
    background: radial-gradient(ellipse at 50% 45%, #eeeeee 0%, var(--map-grey) 60%, rgba(230,230,230,0) 72%);
  }
  .city {
    position: absolute; height: 40px; display: flex; align-items: center;
    font-family: Arial, "Open Sans", sans-serif; font-size: 15px; color: #fff; letter-spacing: 0.01em;
  }
  .city.left { justify-content: flex-start; padding-left: 30px;
    background: linear-gradient(90deg, rgba(255,255,255,0) 0%, #c97a8e 25%, var(--wine-bright) 100%); }
  .city.right { padding-left: 40px;
    background: linear-gradient(90deg, var(--wine-bright) 0%, #b04d68 65%, rgba(255,255,255,0) 100%); }
  .panel {
    position: absolute; left: 687px; top: 183px; width: 513px; height: 489px;
    background: var(--paper); box-shadow: -18px 10px 40px rgba(0,0,0,0.08);
  }
  .panel-accent { position: absolute; left: -6px; top: 54px; width: 6px; height: 399px; background: var(--wine); }
  .features { list-style: none; position: absolute; left: 40px; top: 30px; }
  .features li {
    display: flex; align-items: center; gap: 12px; height: 50px;
    font-size: 12.5px; color: var(--ink);
  }
  .features svg { width: 22px; height: 22px; flex: none; }
  .features b { font-weight: 700; }
</style>
</head>
<body>
<main class="slide">
  <div class="pin-badge" role="img" aria-label="Decorative push pin"></div>

  <div class="brand"><span class="brand-mark"></span><span>Velorin<br>Data<br>Centers</span></div>

  <h1 class="title">Introduction</h1>
  <p class="subtitle">One Of India’s First Dedicated Wholesale Colocation Service Providers</p>

  <nav class="slide-dots" aria-hidden="true">
    <span class="d1"></span><span class="d2"></span><span class="active"></span><span class="d4"></span><span class="d5"></span>
  </nav>

  <div class="india-map" role="img" aria-label="Map of India with pins on data center cities joined by network lines"></div>

  <div class="city left" style="left:131px;top:300px;width:166px;">DELHI&nbsp; (NCR)</div>
  <div class="city left" style="left:83px;top:391px;width:145px;">AHMEDABAD</div>
  <div class="city left" style="left:80px;top:444px;width:148px;padding-left:16px;">MUMBAI: 2 DCs</div>
  <div class="city right" style="left:302px;top:487px;width:174px;">HYDERABAD</div>
  <div class="city left" style="left:148px;top:551px;width:129px;padding-left:18px;">BANGALORE</div>
  <div class="city right" style="left:317px;top:570px;width:167px;padding-left:52px;">CHENNAI</div>

  <section class="panel">
    <div class="panel-accent"></div>
    <ul class="features">
      <li><svg viewBox="0 0 24 24"><circle cx="12" cy="12" r="10" fill="none" stroke="var(--wine)" stroke-width="2"/><path d="M7 12l4 4 9-10" fill="none" stroke="var(--wine)" stroke-width="2.4" stroke-linecap="round"/></svg><span><b>Network of 7 Data Centers</b> to be built <b>in 6 Cities across PAN INDIA</b></span></li>
      <li><svg viewBox="0 0 24 24"><circle cx="12" cy="12" r="10" fill="none" stroke="var(--wine)" stroke-width="2"/><path d="M7 12l4 4 9-10" fill="none" stroke="var(--wine)" stroke-width="2.4" stroke-linecap="round"/></svg><span>Totaling <b>11,500 racks</b> or <b>640,000 sq ft. Built Space</b></span></li>
      <li><svg viewBox="0 0 24 24"><circle cx="12" cy="12" r="10" fill="none" stroke="var(--wine)" stroke-width="2"/><path d="M7 12l4 4 9-10" fill="none" stroke="var(--wine)" stroke-width="2.4" stroke-linecap="round"/></svg><span><b>Purpose-Built Data Centers</b></span></li>
      <li><svg viewBox="0 0 24 24"><circle cx="12" cy="12" r="10" fill="none" stroke="var(--wine)" stroke-width="2"/><path d="M7 12l4 4 9-10" fill="none" stroke="var(--wine)" stroke-width="2.4" stroke-linecap="round"/></svg><span><b>European Class Design and Infrastructure</b></span></li>
      <li><svg viewBox="0 0 24 24"><circle cx="12" cy="12" r="10" fill="none" stroke="var(--wine)" stroke-width="2"/><path d="M7 12l4 4 9-10" fill="none" stroke="var(--wine)" stroke-width="2.4" stroke-linecap="round"/></svg><span><b>Tier III Steadfast Institute Design &amp; Constructed Facility Certified</b></span></li>
      <li><svg viewBox="0 0 24 24"><circle cx="12" cy="12" r="10" fill="none" stroke="var(--wine)" stroke-width="2"/><path d="M7 12l4 4 9-10" fill="none" stroke="var(--wine)" stroke-width="2.4" stroke-linecap="round"/></svg><span><b>Verdant Gold Certified</b> with Low Carbon Footprint</span></li>
      <li><svg viewBox="0 0 24 24"><circle cx="12" cy="12" r="10" fill="none" stroke="var(--wine)" stroke-width="2"/><path d="M7 12l4 4 9-10" fill="none" stroke="var(--wine)" stroke-width="2.4" stroke-linecap="round"/></svg><span>Energy Efficient &amp; Environmentally Sustainable: <b>Design PUE of 1.5</b></span></li>
      <li><svg viewBox="0 0 24 24"><circle cx="12" cy="12" r="10" fill="none" stroke="var(--wine)" stroke-width="2"/><path d="M7 12l4 4 9-10" fill="none" stroke="var(--wine)" stroke-width="2.4" stroke-linecap="round"/></svg><span><b>Modular &amp; Scalable Design Philosophy</b></span></li>
      <li><svg viewBox="0 0 24 24"><circle cx="12" cy="12" r="10" fill="none" stroke="var(--wine)" stroke-width="2"/><path d="M7 12l4 4 9-10" fill="none" stroke="var(--wine)" stroke-width="2.4" stroke-linecap="round"/></svg><span><b>Carrier Neutral</b> (with incoming fiber from multiple carriers)</span></li>
    </ul>
  </section>
</main>
</body>
</html>
```